Business Consultancy Wordpress Design

Small business analysis consultancy.

Looking for a bold, clean design for Wordpress. Final site will only be a few pages, some contact information, services provided and a little background information. Potentially a blog.

Colours to be as per logo, with either black or white as the main colour.

Link is www.brevikadvisory.com

More details to be included in the best few days

Name - Brevik Advisory
Provides - Project Consultancy
Updates

Project Deadline Extended
Reason: I am going to be on holiday with little access to the web over 28/02 - 05/03 and am therefore extending the deadline

Target Market(s)

Business professionals

Industry/Entity Type

Business

Colors

Designer to choose colors to be used in the design.

Requirements
Must have
• Must contain the logo in the header
Footer must fit a 3 column layout in wordpress

Business style, royalty free stock images
Nice to have
• Would like the 1 or 2 column wordpress style layout
Should not have
• must not be blog or magazine style layout or look and feel

```html
<!DOCTYPE html>
<html lang="en">
<head>
<meta charset="utf-8">
<title>Brevik Advisory</title>
<link rel="stylesheet" href="https://fonts.googleapis.com/css2?family=Open+Sans:wght@400;600&family=Arimo:ital,wght@0,400;0,700;1,400&family=Ubuntu:wght@400;500&family=Ubuntu+Condensed&display=swap">
<style>
:root{
  --blue:#0ea5e0;
  --blue-text:#1b9ad6;
  --green:#6ab42d;
  --grey-logo:#6b6e72;
  --text:#444;
  --light:#fff;
  --footer-top:#3c3d41;
  --footer-bottom:#222326;
  --bar:#1e1f21;
}
*{margin:0;padding:0;box-sizing:border-box}
html,body{width:855px;height:1200px;overflow:hidden;background:#fff}
body{position:relative;font-family:Arimo,Arial,sans-serif;color:var(--text)}
.abs{position:absolute}

.brand{left:62px;top:38px;height:32px;display:flex;align-items:center;gap:10px}
.brand-dot{width:30px;height:30px;border-radius:50%;background:var(--blue)}
.brand-name{font-family:Ubuntu,sans-serif;font-size:20px;color:var(--grey-logo);letter-spacing:.3px;text-transform:uppercase}

.search{left:608px;top:44px;width:185px;height:25px;border:1px solid #cfd2d4;font-size:10.5px;color:#888;padding:6px 10px;font-family:Arimo,sans-serif}
.search svg{position:absolute;right:7px;top:7px}

.nav{left:62px;top:96px;width:731px;height:40px;background:var(--blue);display:flex}
.nav a{font-family:"Ubuntu Condensed",sans-serif;color:#fff;text-decoration:none;font-size:13.5px;display:flex;align-items:center;justify-content:center;border-right:1px solid rgba(0,0,0,.08);text-transform:uppercase}
.nav a.active{background:var(--green)}

.hero{left:62px;top:136px;width:731px;height:339px;background:linear-gradient(100deg,#cfd6dc 0%,#b7c0c8 35%,#e4e8ea 60%,#c5ccd3 100%)}
.caption{left:91px;top:333px;width:413px;height:100px;background:rgba(90,95,102,.82);padding:17px 0 0 23px;color:#fff}
.caption h2{font-family:Arimo,sans-serif;font-weight:400;font-size:21px;letter-spacing:.2px;margin-bottom:7px}
.caption p{font-size:12px;line-height:18px}
.dots{left:740px;top:454px;display:flex;gap:3px}
.dots span{width:7px;height:7px;border-radius:50%;background:#333}
.dots span.on{background:#fff;border:1px solid #333}

.heading{font-family:"Open Sans",sans-serif;color:var(--blue-text);font-size:16px;font-weight:400}

.photo{background:linear-gradient(135deg,#c9d3dc,#8f9aa6)}
.welcome-text{left:250px;top:542px;width:543px;font-size:10.5px;line-height:16.3px}
.welcome-text p+p{margin-top:6px}

.post{left:61px;width:440px}
.post .thumb{position:absolute;left:0;top:0;width:96px;height:89px;border:1px solid #ddd;padding:3px;background:#fff}
.post .thumb div{width:100%;height:100%}
.post .body{position:absolute;left:110px;top:0;width:335px}
.post h3{font-family:Arimo,sans-serif;font-weight:400;font-size:12px;color:var(--blue-text);margin-top:1px}
.post p{font-size:8.8px;line-height:15.4px;margin-top:5px}
.meta{display:flex;align-items:center;gap:14px;margin-top:4px;font-size:8.5px;font-style:italic}
.btn{font-style:normal;font-size:9px;border:1px solid #d5d5d5;background:#f1f1f1;padding:2px 6px;display:flex;align-items:center;gap:4px;color:#335}
.btn i{width:7px;height:7px;border-radius:50%;background:var(--blue);display:block}

.about-text{left:581px;top:834px;width:215px;font-size:10.5px;line-height:16.3px}

.footer{left:0;top:958px;width:855px;height:189px;background:linear-gradient(#444549,#2a2b2e)}
.footer-bar{left:0;top:1147px;width:855px;height:53px;background:var(--bar);border-top:1px solid #3a3b3e}
.fcol{top:990px;font-family:Ubuntu,sans-serif;color:#eee}
.fcol h4{font-family:Arimo,sans-serif;font-weight:700;font-size:11px;margin-bottom:11px;color:#fff}
.fcol li{list-style:none;font-size:11px;line-height:20.5px;font-weight:400}
.fcol p{font-size:11px;line-height:20px;width:200px;letter-spacing:-.2px}
.field{left:582px;top:1058px;width:193px;height:25px;background:#fff}
.subscribe{left:681px;top:1097px;width:94px;height:25px;background:#2e8fe0;color:#fff;font-family:"Ubuntu Condensed",sans-serif;font-size:14px;display:flex;align-items:center;justify-content:center}
.copy{left:63px;top:1166px;font-size:10.5px;color:#fff}
.social{top:1160px;width:26px;height:26px}
</style>
</head>
<body>

<div class="abs brand"><span class="brand-dot"></span><span class="brand-name">Brevik Advisory</span></div>

<div class="abs search">Search..
  <svg width="10" height="10" viewBox="0 0 10 10"><circle cx="4" cy="4" r="3" fill="none" stroke="#888" stroke-width="1.3"/><line x1="6.3" y1="6.3" x2="9.3" y2="9.3" stroke="#888" stroke-width="1.5"/></svg>
</div>

<nav class="abs nav">
  <a class="active" style="width:77px">Home</a>
  <a style="width:104px">About Us</a>
  <a style="width:100px">Services</a>
  <a style="width:102px">Contact</a>
  <a style="width:80px">Blog</a>
  <a style="width:85px">Links</a>
</nav>

<div class="abs hero" role="img" aria-label="Smiling businessman in a bright office with colleagues blurred in the background"></div>
<div class="abs caption">
  <h2>DUIS AUTEM VEL EUM IRURE DOLOR</h2>
  <p>Jerta baditaut onsequser untur magni dolores eioquie voluptate msei nesciunt. Voluptatem accusantium dolorem lorem. consuetudium.</p>
</div>
<div class="abs dots"><span class="on"></span><span></span><span></span><span></span></div>

<h2 class="abs heading" style="left:62px;top:500px">Welcome to Our Website</h2>
<div class="abs photo" style="left:62px;top:544px;width:165px;height:96px" role="img" aria-label="Business team meeting around a table"></div>
<div class="abs welcome-text">
  <p>Duis autem vel eum iriure dolor in hendrerit in vulputate velit esse molestie consequat, vel illunm dolore eu feugiat nullfac ilis.&nbsp; Typi non habent claritatem. Nam liber tempor cum soluta nobis eleifend.</p>
  <p>Duis autem vel eum iriure dolor in hendrerit in vulputate velit esse molestie consequat, vel illun dolore eu feugiat nullaacili sis at vero eros et accumsan et iusto odio dignissim qui blandit praeisent luptatum zzril delenit augue duis dolore te fegait nilla facilisi. Claritas est etiam processus dynamicus, qui sequitur mutationem consuetudium lectorum. Mirum est notarqu am littera gothica quam nunc putamus parum claram, anteposuerit litterarum formas humanitatis Claritas est.</p>
</div>

<h2 class="abs heading" style="left:61px;top:677px">Blog Posts</h2>

<article class="abs post" style="top:713px">
  <div class="thumb"><div class="photo" role="img" aria-label="Smiling business team"></div></div>
  <div class="body">
    <h3>Suspendisse eu erat quam. Vivamus porttitor eros quis.</h3>
    <p>Suspendisse eu erat quam. Vivamus porttitor eros quis nisi lacinia sed interdum uam a orci quis nisi sagittis sagittis. Etiam adipiscing, justo quis feugiat.Suspend amus porttitor eros quis nisi lacinia sed interdum lorem vulputate.</p>
    <div class="meta"><span>Posted on 02 June, 2013</span><span class="btn"><i></i>Follow</span><span class="btn">Like</span></div>
  </div>
</article>

<article class="abs post" style="top:824px">
  <div class="thumb"><div class="photo" role="img" aria-label="Business handshake over a laptop"></div></div>
  <div class="body">
    <h3>Suspendisse eu erat quam. Vivamus porttitor eros quis.</h3>
    <p>Suspendisse eu erat quam. Vivamus porttitor eros quis nisi lacinia sed interdum uam a orci quis nisi sagittis sagittis. Etiam adipiscing, justo quis feugiat.Suspend amus porttitor eros quis nisi lacinia sed interdum lorem vulputate.</p>
    <div class="meta"><span>Posted on 02 June, 2013</span><span class="btn"><i></i>Follow</span><span class="btn">Like</span></div>
  </div>
</article>

<h2 class="abs heading" style="left:582px;top:679px">About Us</h2>
<div class="abs" style="left:582px;top:713px;width:211px;height:104px;background:linear-gradient(135deg,#dfe6ee,#2d4868)" role="img" aria-label="Business people shaking hands"></div>
<p class="abs about-text">Consectet adipisicing elit, sed do eiusmod ut e nim ad minim veniam. tempor incididunt ut labo re et dolore magna aliqua. Ut enim ad minim ve niam. Quis nostrud exercitation ullamco laboris nisi ut aliquip ex ea commodo consequat.</p>

<footer class="abs footer"></footer>
<div class="abs fcol" style="left:62px">
  <h4>Links</h4>
  <ul><li>Typi non haben</li><li>Successful Campaigns</li><li>New Campaigns</li><li>Ending Soon</li><li>Most Funded Campaigns</li></ul>
</div>
<div class="abs fcol" style="left:236px;top:989px">
  <h4>Links Goods</h4>
  <ul><li>Typi non haben</li><li>Contact Us</li><li>Help</li><li>Privacy Policy</li><li>Terms Of Service</li></ul>
</div>
<div class="abs fcol" style="left:393px;top:989px">
  <h4>Links Services</h4>
  <ul><li>Typi non haben</li><li>Contact Us</li><li>Help</li><li>Privacy Policy</li><li>Terms Of Service</li></ul>
</div>
<div class="abs fcol" style="left:582px;top:988px">
  <h4>Newsletter Signup</h4>
  <p>Stay in touch with us by signing up for our quarterly newsletter!</p>
</div>
<div class="abs field"></div>
<div class="abs subscribe">SUBSCRIBE</div>

<div class="abs footer-bar"></div>
<p class="abs copy">Copyright ©2013. All Rights Reserved.</p>
<span class="abs social" style="left:598px;background:#2f55a4"></span>
<span class="abs social" style="left:633px;background:#1d9bd9"></span>
<span class="abs social" style="left:668px;background:#f37021"></span>
<span class="abs social" style="left:703px;background:#d62a2a"></span>

</body>
</html>
```